Sponsorship and registration document for Charity Golf Day 2022

The project requires 2 documents to be updated to look more graphically savvy and professionally presentable.
1. Charity golf day sponsorship document
2. One page registration document.
The text has been completed. Text not to be changed - just graphics.
New images would be preferred.
The logos have been provided.

Target Market(s)

Corporate Sponsors and Golf players

Requirements
Must have
• Golf Theme

```html
<!DOCTYPE html>
<html lang="en">
<head>
<meta charset="utf-8">
<title>Charity Golf Day – Sponsorship Proposal</title>
<link href="https://fonts.googleapis.com/css2?family=Roboto+Condensed:wght@400;700&family=Roboto:wght@300;400;500;700&display=swap" rel="stylesheet">
<style>
:root{
  --navy:#34405a;
  --navy-dark:#2b3550;
  --orange:#f39a1e;
  --paper:#ffffff;
  --ink:#3a3f4b;
  --muted:#6b7180;
  --backdrop:#e9e7e3;
  --grass:#5f9a3a;
  --grass-light:#9cc861;
  --sky:#cfe0ee;
}
*{box-sizing:border-box;margin:0;padding:0}
html,body{width:1200px;height:900px;overflow:hidden;background:var(--backdrop)}
body{font-family:"Roboto",Arial,sans-serif;color:var(--ink);position:relative}
.page{position:absolute;top:181px;width:380px;height:538px;background:var(--paper);overflow:hidden;box-shadow:0 2px 10px rgba(0,0,0,.12)}
.cover{left:20px}
.spread-left{left:420px}
.spread-right{left:800px;border-left:1px solid #e2e2e2}
.heading{font-family:"Roboto Condensed",Arial,sans-serif}

/* Cover */
.cover-header{height:100px;background:var(--navy);text-align:center;padding-top:24px}
.cover-title{font-family:"Roboto Condensed",Arial,sans-serif;font-weight:700;color:var(--orange);font-size:34px;letter-spacing:.5px;line-height:1}
.cover-date{color:#fff;font-family:"Roboto Condensed",Arial,sans-serif;font-weight:700;font-size:14px;margin-top:6px;line-height:1.15}
.cover-photo{height:280px;background:linear-gradient(180deg,var(--sky) 0%,#a9c6a0 35%,var(--grass) 70%,#3f6f2a 100%)}
.cover-brand{display:flex;align-items:center;justify-content:center;gap:6px;margin-top:12px;color:var(--navy);font-weight:500;font-size:13px}
.brand-dot{width:20px;height:20px;border-radius:50%;background:var(--orange)}
.proposal-band{position:relative;margin:14px auto 0;width:330px;height:26px}
.proposal-band svg{position:absolute;inset:0}
.proposal-band span{position:relative;display:block;text-align:center;color:#fff;font-family:"Roboto Condensed",Arial,sans-serif;font-weight:700;font-size:19px;line-height:26px;letter-spacing:.3px}
.cover-sub{text-align:center;color:var(--orange);font-family:"Roboto Condensed",Arial,sans-serif;font-weight:700;font-size:13px;margin-top:6px}
.cover-tag{text-align:center;color:var(--navy);font-size:11.5px;line-height:1.3;margin-top:5px}
.cover-footer{position:absolute;left:0;right:0;bottom:0;height:26px}
.cover-footer svg{position:absolute;inset:0}
.cover-url{position:absolute;right:30px;bottom:6px;color:#fff;font-size:11px;display:flex;align-items:center;gap:6px}

/* Spread left */
.spread-photo{height:160px;background:linear-gradient(180deg,#2f4a22 0%,#557d33 35%,#8fbf4e 65%,#6ea23a 100%)}
.photo-rule{height:4px;background:var(--orange);width:60%}
.left-body{padding:14px 18px 0 18px}
.intro{font-size:10.5px;line-height:1.4;color:var(--navy-dark)}
.intro-rule{width:120px;height:2px;background:var(--navy);margin:5px 0 10px}
.body-text{font-size:6.6px;line-height:1.45;color:var(--ink);margin-bottom:7px}
.body-text b{color:var(--navy)}
.format-title{font-size:8px;font-weight:500;color:var(--navy);margin:4px 0 6px}
.format-list{list-style:none}
.format-list li{display:flex;align-items:center;gap:7px;font-size:8px;margin-bottom:6px;color:var(--ink)}
.format-icon{width:15px;height:15px;background:var(--orange);border-radius:2px;flex:none}
.signoff{margin-top:10px;font-size:6.6px;line-height:1.4}
.signoff .role{font-size:5.6px;color:var(--muted);line-height:1.4}
.signoff strong{font-weight:500}
.page-foot{position:absolute;left:0;right:0;bottom:0;height:6px;background:var(--navy)}

/* Spread right */
.why-panel{position:relative;height:160px}
.why-panel svg{position:absolute;inset:0}
.why-content{position:relative;padding:22px 0 0 22px;width:240px;color:#fff}
.why-title{color:var(--orange);font-family:"Roboto Condensed",Arial,sans-serif;font-size:11.5px;font-weight:400}
.why-rule{width:50px;height:2px;background:var(--orange);margin:6px 0 10px}
.dot-list{list-style:none}
.dot-list li{font-size:6.3px;line-height:1.3;margin-bottom:4px;padding-left:6px;position:relative}
.dot-list li::before{content:"•";position:absolute;left:0}
.right-body{padding:14px 22px 0 22px}
.ask-title{font-size:10.5px;color:var(--navy-dark);margin-bottom:8px}
.ask-list li{font-size:6.5px;color:var(--ink);margin-bottom:3.5px}
.achieve{background:var(--navy);border-radius:5px;margin:10px 0 14px;padding:8px 12px 9px;color:#fff}
.achieve-title{text-align:center;color:var(--orange);font-family:"Roboto Condensed",Arial,sans-serif;font-size:10.5px;margin-bottom:6px}
.achieve-item{display:flex;gap:5px;font-size:6px;line-height:1.3;margin-bottom:5px}
.achieve-item .arrow{width:7px;height:7px;border-radius:50%;background:var(--orange);flex:none;margin-top:1px;position:relative}
.achieve-item .arrow::after{content:"";position:absolute;left:2px;top:1.5px;border-left:3px solid var(--navy);border-top:2px solid transparent;border-bottom:2px solid transparent}
.achieve-item .amount{color:var(--orange);font-weight:700;font-size:8px;white-space:nowrap}
.more-info{margin-top:12px;font-size:6.3px;color:var(--ink)}
.more-info b{display:block;color:var(--navy-dark);font-weight:500}
</style>
</head>
<body>

<!-- Cover -->
<section class="page cover">
  <header class="cover-header">
    <h1 class="cover-title">CHARITY GOLF DAY</h1>
    <p class="cover-date">FRIDAY 25 MARCH 2022<br>Elmhurst Golf Club</p>
  </header>
  <div class="cover-photo" role="img" aria-label="Golfer in a yellow shirt finishing his swing on a tree-lined fairway"></div>
  <div class="cover-brand"><span>Kingsford Service Club</span><span class="brand-dot"></span></div>
  <div class="proposal-band">
    <svg viewBox="0 0 330 26" preserveAspectRatio="none" aria-hidden="true">
      <polygon points="0,26 6,0 18,0 12,26" fill="var(--orange)"/>
      <polygon points="312,26 318,0 330,0 324,26" fill="var(--orange)"/>
      <polygon points="8,26 14,0 322,0 316,26" fill="var(--navy)"/>
    </svg>
    <span>SPONSORSHIP PROPOSAL</span>
  </div>
  <p class="cover-sub">SUPPORTING PROSTATE CANCER RESEARCH</p>
  <p class="cover-tag">Help us hit prostate cancer off the green<br>and beat the most common cancer in Australian men.</p>
  <footer class="cover-footer">
    <svg viewBox="0 0 380 26" preserveAspectRatio="none" aria-hidden="true">
      <rect x="0" y="4" width="200" height="22" fill="var(--orange)"/>
      <polygon points="180,26 196,0 380,0 380,26" fill="var(--navy)"/>
    </svg>
    <span class="cover-url">
      <svg width="10" height="10" viewBox="0 0 10 10" aria-hidden="true"><circle cx="5" cy="5" r="4.3" fill="none" stroke="#fff" stroke-width=".9"/><ellipse cx="5" cy="5" rx="1.8" ry="4.3" fill="none" stroke="#fff" stroke-width=".8"/><line x1=".7" y1="5" x2="9.3" y2="5" stroke="#fff" stroke-width=".8"/></svg>
      www.kingsfordclub.org/golf-day
    </span>
  </footer>
</section>

<!-- Inside left -->
<section class="page spread-left">
  <div class="spread-photo" role="img" aria-label="Golf green with a sand bunker framed by gum trees"></div>
  <div class="photo-rule"></div>
  <div class="left-body">
    <p class="intro">Join us for an exclusive day on the private Elmhurst Golf Course, with all proceeds going to support Prostate Cancer Research, Awareness and Support.</p>
    <div class="intro-rule"></div>
    <p class="body-text">The Kingsford Service Club will again be holding its Charity Golf Day with all proceeds used to support the Prostate Cancer Research, awareness and Support Programs. The venue will be the prestigious Elmhurst Golf Club on Friday 25 March 2022, with a shotgun start at 8:00 am.</p>
    <p class="body-text">We have enclosed for your information a copy of our promotional sponsor packages that outline the event, sponsorship package options and inclusions.</p>
    <p class="format-title">THE FORMAT OF THE DAY INVOLVES:</p>
    <ul class="format-list">
      <li><span class="format-icon"></span>Player registration, refreshments and light breakfast from 7:00am</li>
      <li><span class="format-icon"></span>Ambrose competition starting at 8:00am</li>
      <li><span class="format-icon"></span>Two Course lunch and presentations in the club house from 12:30pm</li>
    </ul>
    <p class="body-text" style="margin-top:8px">Your commitment to supporting health programs in our community is truly appreciated. With assistance from sponsors such as yourself, we will continue to see improvements in the support and treatment for men and their families with prostate cancer.</p>
    <p class="body-text">We hope that you will consider supporting the worthwhile event that is open to any organisation or individual who wishes to enjoy the benefits of playing golf at the prestigious Elmhurst Golf Club. For more information, please check the website <b>www.kingsfordclub.org/golf-day</b> or should you wish to discuss any aspect of the event, please contact me on <b>0400 555 182</b>.</p>
    <div class="signoff">
      <p><strong>Yours sincerely,</strong></p>
      <p><strong>Helena (Marris) Whitcombe Convener</strong></p>
      <p class="role">Co-President 2021-2022<br>Secretary 2021-2022<br>Kingsford Service Club</p>
    </div>
  </div>
  <div class="page-foot"></div>
</section>

<!-- Inside right -->
<section class="page spread-right">
  <div class="why-panel">
    <svg viewBox="0 0 380 160" preserveAspectRatio="none" aria-hidden="true">
      <defs>
        <linearGradient id="ballPhoto" x1="0" y1="0" x2="0" y2="1">
          <stop offset="0" stop-color="#d7e7a6"/>
          <stop offset=".5" stop-color="#8dbb45"/>
          <stop offset="1" stop-color="#4f8a2a"/>
        </linearGradient>
      </defs>
      <rect x="0" y="0" width="380" height="160" fill="var(--navy)"/>
      <polygon points="238,0 380,0 380,160 340,160" fill="url(#ballPhoto)"/>
      <polygon points="0,0 238,0 246,12 0,12" fill="var(--orange)"/>
      <polygon points="0,153 330,153 336,160 0,160" fill="var(--orange)"/>
    </svg>
    <div class="why-content">
      <h2 class="why-title">WHY PROSTATE CANCER?</h2>
      <div class="why-rule"></div>
      <ul class="dot-list">
        <li>Prostate cancer is the most diagnosed cancer in Australian men.</li>
        <li>Approximately 20,000 Australian men are diagnosed with prostate cancer each year.</li>
        <li>Over 200,000 Australian men are living with a diagnosis prostate cancer.</li>
        <li>95% of Australian men diagnosed with prostate cancer survive for at least 5 years.</li>
        <li>Almost 3,500 Australian men die of prostate cancer each year.</li>
      </ul>
    </div>
    <span role="img" aria-label="Golf club beside a ball on the grass" style="position:absolute;right:0;top:0;width:140px;height:160px"></span>
  </div>
  <div class="right-body">
    <h3 class="ask-title">Why are we asking you to be involved?</h3>
    <ul class="dot-list ask-list">
      <li>Every day 54 Australian men will be told they have prostate cancer</li>
      <li>70% of research applications are unfunded</li>
      <li>1 in 6 men will suffer from prostate cancer</li>
      <li>9 families lose a loved one to prostate cancer every day</li>
      <li>Only 1 in 3 men have access to a specialist nurse</li>
    </ul>
    <div class="achieve">
      <h3 class="achieve-title">WHAT THIS FUNDRAISING EVENT CAN ACHIEVE</h3>
      <div class="achieve-item"><span class="arrow"></span><p><span class="amount">$12,500</span> – could provide funding for a researcher working for one month on a project to reduce side – effects post treatment.</p></div>
      <div class="achieve-item"><span class="arrow"></span><p><span class="amount">$30,000</span> – could provide finding for a senior scientist for three months working on a project to improve treatments for prostate cancer that has spread to the bones.</p></div>
      <div class="achieve-item"><span class="arrow"></span><p><span class="amount">$50,000</span> – could fund a project to improve early – diagnosis for men with a family history of prostate cancer</p></div>
    </div>
    <p class="body-text">Proceeds from this event will be donated to Prostate Cancer Research Group at the Life Sciences Research Institute, Westbrook University, to fund world leading, innovative research and to support men and their families affected by prostate cancer.</p>
    <p class="body-text">Their innovative research program has a strong translational approach, involving lab-based studies with tissues donated by patients with prostate cancer. Their collaborative studies with clinicians and patient advocates address questions that are relevant to patient care. The findings have the potential to improve the management and outcomes of men with different stages of prostate cancer. Recent studies have informed international guidelines for diagnosis of prostate cancer and led to new clinical trials.</p>
    <p class="more-info">For more information visit their website:<b>www.westbrook.edu/life-sciences/prostate-cancer-research-group/research</b></p>
  </div>
  <div class="page-foot"></div>
</section>

</body>
</html>
```